Vexo App Form Input Screens - Sleek Clean Design

We have a input form that we would like to transpose into an Vexo App. We have a programmer to do the screens but we need to take this very field heavy form and get it into clean design input screens (We can as many screens as make sense). We want to design to be slick and intuitive. This will be used by young guys who enjoy a gaming atmosphere. But the design has to be easy enough to be completely intuitive to a novice user. The Company likes to do things with Sky Blue colors. Also OK to incorporate burnt orange/yellow (Think glowing sun).

Target Market(s)

18-25 year old males - These guys go door to door and input this data all day

Industry/Entity Type

Solar Energy

Number of Pages Required

5+ page

Font styles to use
Sans Serif

Colors
0355a3
3277b5
85acd3
d0dfed
faa54b
ffc214
f68e4d

Requirements
Must have
• Clean simple sleek Designs - Drop Down Examples. The background and fields have to have distinct colors because these guys will be outside most of the time and if the design is not contrasted enough, it will be hard for them to see.
Nice to have
• Fun ways to incorporate the Glowing Sun Colors (Subtle)
Should not have
• Should not look like Powerpoint

```html
<!DOCTYPE html>
<html lang="en">
<head>
<meta charset="utf-8">
<title>Vexo – Measure Information</title>
<link href="https://fonts.googleapis.com/css2?family=Open+Sans:ital,wght@0,400;0,600;0,700;1,400&display=swap" rel="stylesheet">
<style>
  :root{
    --navy:#033f7c;
    --navy-deep:#022d5c;
    --blue-text:#0a4a8c;
    --sun:#ffc214;
    --sun-dark:#f5b400;
    --field:#eef3f8;
    --rule:#e3e9f0;
    --ink:#1c2430;
    --muted:#8a97a6;
    --white:#ffffff;
    --scene-top:#0a4f99;
    --scene-bottom:#1466b3;
  }
  *{box-sizing:border-box;margin:0;padding:0}
  html,body{width:1200px;height:900px;overflow:hidden}
  body{font-family:"Open Sans",Arial,sans-serif;background:var(--navy);position:relative}

  .topbar{position:absolute;left:0;top:0;width:1200px;height:106px}
  .record-label{position:absolute;left:18px;top:38px;color:var(--white);font-size:21px;line-height:32px}
  .record-tabs{position:absolute;left:152px;top:34px;height:44px;display:flex;background:var(--navy-deep);border-radius:3px;overflow:hidden}
  .record-tab{height:44px;display:flex;align-items:center;padding:0 19px;color:#dbe6f2;font-size:19px;border-right:1px solid #0b3f75}
  .record-tab:last-child{border-right:none}
  .record-tab.is-active{background:var(--sun);color:#111;font-weight:700;padding:0 16px}
  .record-tab svg{margin-left:8px}
  .submit-btn{position:absolute;right:0;top:0;width:152px;height:105px;background:var(--sun);border-bottom:5px solid var(--sun-dark);color:#1a1a1a;font-size:27px;display:flex;align-items:center;justify-content:center;padding-top:2px}

  .sidebar{position:absolute;left:0;top:106px;width:227px;height:794px;padding-top:11px}
  .nav-item{height:82px;display:flex;align-items:center;padding-left:22px;color:#d5e2f0;font-size:18px;line-height:21px}
  .nav-item svg{width:38px;height:38px;margin-right:10px;flex:none}
  .nav-item.is-active{background:var(--sun);color:#111;font-weight:700}
  .nav-scene{position:absolute;left:0;top:504px;width:227px;height:290px;
    background:linear-gradient(180deg,var(--scene-top) 0%,var(--scene-bottom) 100%)}

  .panel{position:absolute;left:227px;top:106px;width:973px;height:794px;background:var(--white);border-top-left-radius:14px}
  .panel-title{position:absolute;left:54px;top:34px;width:865px;font-size:24px;line-height:32px;font-weight:600;color:var(--blue-text);padding-bottom:1px;border-bottom:2px solid var(--rule)}
  .field{position:absolute}
  .field-label{font-size:21px;color:var(--ink);line-height:28px;margin-bottom:8px;white-space:nowrap}
  .field-box{height:46px;background:var(--field);border-radius:3px;display:flex;align-items:center;padding:0 14px;font-size:19px}
  .field-box.select{color:var(--blue-text);justify-content:space-between}
  .field-box.placeholder{color:var(--muted);font-style:italic}
</style>
</head>
<body>
  <header class="topbar">
    <div class="record-label">Record Type</div>
    <nav class="record-tabs">
      <div class="record-tab is-active">Solvana</div>
      <div class="record-tab">BrightPath</div>
      <div class="record-tab">HomeCrest</div>
      <div class="record-tab">Cash</div>
      <div class="record-tab">Other
        <svg width="16" height="16" viewBox="0 0 16 16"><path d="M2 14l1-4 8-8 3 3-8 8z" fill="#fff"/></svg>
      </div>
    </nav>
    <div class="submit-btn">Submit</div>
  </header>

  <aside class="sidebar">
    <div class="nav-item">
      <svg viewBox="0 0 38 38"><circle cx="19" cy="11" r="8" fill="#dbe6f2"/><path d="M3 37c0-9 7-15 16-15s16 6 16 15z" fill="#dbe6f2"/></svg>
      <span>Customer<br>Information</span>
    </div>
    <div class="nav-item">
      <svg viewBox="0 0 38 38" fill="none" stroke="#dbe6f2" stroke-width="3.5" stroke-linecap="round"><path d="M5 33L25 13"/><circle cx="29" cy="9" r="5"/><path d="M6 6l26 26"/></svg>
      <span>Utility<br>Information</span>
    </div>
    <div class="nav-item">
      <svg viewBox="0 0 38 38"><circle cx="19" cy="19" r="17" fill="#dbe6f2"/><path d="M22 6L11 21h7l-3 11 11-15h-7z" fill="#033f7c"/></svg>
      <span>Electrical<br>Information</span>
    </div>
    <div class="nav-item">
      <svg viewBox="0 0 38 38" fill="none" stroke="#dbe6f2" stroke-width="3"><rect x="6" y="6" width="26" height="26"/><path d="M6 6l26 26M32 6L6 32"/><g fill="#dbe6f2"><circle cx="6" cy="6" r="5"/><circle cx="32" cy="6" r="5"/><circle cx="6" cy="32" r="5"/><circle cx="32" cy="32" r="5"/></g></svg>
      <span>System Details</span>
    </div>
    <div class="nav-item">
      <svg viewBox="0 0 38 38" fill="none" stroke="#dbe6f2" stroke-width="3"><rect x="3" y="3" width="32" height="22" rx="2"/><path d="M14 3v22M24 3v22M3 14h32M19 25v8M11 35h16"/></svg>
      <span>Roof Mount</span>
    </div>
    <div class="nav-item is-active">
      <svg viewBox="0 0 38 38"><path d="M4 31L31 4l4 4L8 35z" fill="#111"/><path d="M4 8l4-4 27 27-4 4z" fill="#111"/></svg>
      <span>Measure<br>Information</span>
    </div>
    <div class="nav-scene" role="img" aria-label="Illustration of a solar-panelled house among trees and buildings under the sun"></div>
  </aside>

  <main class="panel">
    <h1 class="panel-title">Measure Information</h1>

    <div class="field" style="left:55px;top:98px;width:421px">
      <div class="field-label">Do trees need to be cut?</div>
      <div class="field-box select">Choose
        <svg width="16" height="10" viewBox="0 0 16 10"><path d="M2 2l6 6 6-6" fill="none" stroke="#0a4a8c" stroke-width="3"/></svg>
      </div>
    </div>

    <div class="field" style="left:499px;top:98px;width:420px">
      <div class="field-label">When? (New site survey will be required)</div>
      <div class="field-box placeholder">When?</div>
    </div>

    <div class="field" style="left:55px;top:210px;width:864px">
      <div class="field-label">Instructions for Measure/Installation crew</div>
      <div class="field-box placeholder">Instructions for Measure/Installation crew</div>
    </div>
  </main>
</body>
</html>
```